"STYLE NIBBLES" courses banner ads

Creation of 6 web banners for google display network and 1 image to be used on FaceBook.

Our website: http://www.vormlab-example.org/
Our facebook: https://www.facebook.com/vormlab/

The banners are meant to attract consumers to click and go to our landing page to find out more about our series of short courses training to be held in 4/5* hotels. The courses to be trained are Colour and Styling, Fabric Care and Leather Care.

Example of the short courses landing page: http://www.vormlab-example.org/special-holiday-season-courses/

Target Market(s)

Females, 25-55 years old, interested in learning fashion styling, fabric care

Industry/Entity Type

Fashion

Font styles to use
Sans Serif

Colors
ec1f27
757575

Requirements
Must have
• Image used should have people and are happy/smiling.
• Some samples of pass banner ads images will be included: see the fabric care and open house samples
• Corporate colours are red, grey and black but addition of complementary colours will be great. Not necessary to use all the three corporate colours at the same time.
• Logos - to be provided (VORMLAB)
• TEXT:
• Style Nibbles
• Short Courses held in hotels in June and July 2017
• Find out more!
Nice to have
• Asian person(s) in the image - please propose the stock image if necessary.
Should not have
• clip art
• fashion runway

```html
<!DOCTYPE html>
<html lang="en">
<head>
<meta charset="utf-8">
<title>Style Nibbles – Short Courses Banners</title>
<link rel="stylesheet" href="https://fonts.googleapis.com/css2?family=Tinos:wght@400;700&family=Oswald:wght@400&family=Open+Sans:wght@400&display=swap">
<style>
  :root {
    --brand-red: #ec1f27;
    --ink: #1a1a1a;
    --grey: #757575;
    --paper: #ffffff;
    --cream: #f6f1e8;
    --canvas-bg: #e4e4e4;
    --serif: "Tinos", "Times New Roman", serif;
    --condensed: "Oswald", "Arial Narrow", sans-serif;
    --ui: "Open Sans", Arial, sans-serif;
  }
  html, body {
    margin: 0;
    padding: 0;
    width: 1200px;
    height: 1200px;
    overflow: hidden;
    background: var(--canvas-bg);
  }
  .artboard {
    position: relative;
    width: 1200px;
    height: 1200px;
  }
  .cover-image {
    position: absolute;
    left: 50px;
    top: 190px;
    width: 1100px;
    height: 407px;
    box-shadow: 0 6px 24px rgba(0,0,0,0.18);
  }
  .leaderboard {
    position: absolute;
    left: 30px;
    top: 780px;
    width: 1140px;
    height: 146px;
    box-shadow: 0 6px 24px rgba(0,0,0,0.18);
  }
  .serif { font-family: var(--serif); }
  .condensed { font-family: var(--condensed); }
  .ui { font-family: var(--ui); }
  .red { fill: var(--brand-red); }
  .ink { fill: var(--ink); }
  .white { fill: var(--paper); }
</style>
</head>
<body>
<main class="artboard">

  <!-- Facebook cover image -->
  <svg class="cover-image" viewBox="0 0 920 340" xmlns="http://www.w3.org/2000/svg">
    <defs>
      <linearGradient id="coverPhotoTone" x1="0" y1="0" x2="1" y2="0">
        <stop offset="0" stop-color="#c9d6e4"/>
        <stop offset="0.35" stop-color="#e8ddd0"/>
        <stop offset="0.7" stop-color="#f1ede8"/>
        <stop offset="1" stop-color="#ffffff"/>
      </linearGradient>
    </defs>
    <rect class="white" x="0" y="0" width="920" height="340"/>
    <rect x="0" y="0" width="700" height="320" fill="url(#coverPhotoTone)" role="img"
          aria-label="Photo of a smiling young Asian woman with a tape measure in a bright studio, clothes rails behind her"/>

    <text class="serif red" x="448" y="186" font-size="33" font-weight="700">STYLE NIBBLES</text>
    <text class="condensed ink" x="446" y="242" font-size="48" letter-spacing="1">JUNE &amp; JULY 2017</text>

    <rect class="red" x="646" y="280" width="157" height="25" rx="4"/>
    <text class="ui white" x="724.5" y="297.5" font-size="14" text-anchor="middle">Find Out More</text>

    <text class="serif red" font-size="34" transform="translate(862,22) rotate(90)">SHORT COURSES</text>
    <text class="serif ink" font-size="25" transform="translate(835,68) rotate(90)">HELD IN HOTELS</text>
    <rect class="ink" x="848" y="282" width="4" height="40"/>

    <rect class="red" x="0" y="320" width="920" height="20"/>
  </svg>

  <!-- Display network leaderboard -->
  <svg class="leaderboard" viewBox="0 0 1327 170" xmlns="http://www.w3.org/2000/svg">
    <defs>
      <linearGradient id="bannerPhotoTone" x1="0" y1="0" x2="1" y2="0">
        <stop offset="0" stop-color="#bccde0"/>
        <stop offset="0.22" stop-color="#e6ddd2"/>
        <stop offset="0.45" stop-color="#f6f1e8"/>
        <stop offset="0.75" stop-color="#fbf9f5"/>
        <stop offset="1" stop-color="#ffffff"/>
      </linearGradient>
    </defs>
    <rect x="0" y="0" width="1327" height="170" fill="url(#bannerPhotoTone)" role="img"
          aria-label="Photo of a smiling young Asian woman beside a tailor's dummy and clothes rails, fading into cream"/>

    <text class="serif ink" x="532" y="92" font-size="48" text-anchor="middle" letter-spacing="2">VORMLAB</text>
    <text class="serif ink" x="532" y="138" font-size="25" text-anchor="middle" letter-spacing="0.5">STYLE NIBBLES</text>

    <text class="serif red" x="1108" y="59" font-size="40" text-anchor="end">SHORT COURSES</text>
    <text class="serif ink" x="1108" y="90" font-size="31" text-anchor="end">HELD IN HOTELS</text>
    <rect class="ink" x="1110" y="69" width="217" height="6"/>
    <text class="condensed ink" x="1108" y="128" font-size="28" text-anchor="end">JUNE &amp; JULY 2017</text>

    <rect class="red" x="1156" y="118" width="123" height="19" rx="3"/>
    <text class="ui white" x="1217.5" y="131.5" font-size="11" text-anchor="middle">Find Out More</text>

    <rect class="red" x="0" y="152" width="1327" height="18"/>
  </svg>

</main>
</body>
</html>
```